Veltra Homes Real Estate Brokerage Recruiting Flyer

We are a real estate brokerage looking to hire more real estate agents. We need to list everything we have to offer as a company so real estate agents will join our company. this is our company website: www.Veltrahomes.example .

100% COMMISSION NO MONTHLY FEE
$450 Flat Transaction FEE

What We Offer:
24/7 Office Access
Free E & O Insurance for 1st Year
Free Online CE and PLE
Free 1,000 Business Cards
Free Professional Social Media Marketing
Free Printing, Scanning, and Copies
Free Buyer and Seller Presentation Packages
Free Papervane Cloud Based Document Management Access
Access to our Internal Brokerage Forum
Company Profit Sharing!
Private Offices Available to Rent

*Lead Generation Software with over 3,000 Leads
*10 Leads to Start
* Free Personal CRM and Website
*Restrictions and Rules apply

Company Address:
4817 Marlow Creek Road
Suite 412
Fairfax, VA 22147
Phone: 703-241-7086
email: info@veltrahomes.example

Target Market(s)

Real Estate Agents

Industry/Entity Type

Real Estate

Colors
0555a3
ffffff

Requirements
Must have
• 100% COMMISSION NO MONTHLY FEE
$450 Flat Transaction FEE

What We Offer:
24/7 Office Access
Free Online CE and PLE
Free 1,000 Business Cards
Company Profit Sharing!

*10 Leads to Start

Company Address:
4817 Marlow Creek Road
Suite 412
Fairfax, VA 22147
Phone: 703-241-7086

```html
<!DOCTYPE html>
<html lang="en">
<head>
<meta charset="utf-8">
<title>Veltra Homes – Agent Recruiting Flyer</title>
<link href="https://fonts.googleapis.com/css2?family=Montserrat:wght@600;700;800;900&family=Open+Sans:wght@400;600;700&display=swap" rel="stylesheet">
<style>
  :root{
    --navy:#2a3a7e;
    --brand:#0555a3;
    --yellow:#f5b21b;
    --sky:#c7e7f1;
    --white:#ffffff;
    --ink:#25305e;
    --stage:#e4e5e7;
  }
  *{box-sizing:border-box;margin:0;padding:0}
  html,body{width:1200px;height:1200px;overflow:hidden;background:var(--stage)}
  .flyer{position:absolute;left:160px;top:30px;width:880px;height:1140px;background:var(--white);overflow:hidden;font-family:"Open Sans",Arial,sans-serif;color:var(--ink)}
  .photo-team{position:absolute;left:330px;top:0;width:550px;height:420px;background:linear-gradient(160deg,#f2f4f7 0%,#d9dfe8 45%,#6f7fa6 100%)}
  .photo-house{position:absolute;left:0;top:190px;width:400px;height:230px;background:linear-gradient(180deg,#dfe7ee 0%,#b8c1c8 45%,#6d7a69 100%)}
  .logo{position:absolute;left:40px;top:40px;width:300px;height:110px;border:3px solid var(--brand);border-radius:16px;background:var(--white);display:flex;align-items:center;justify-content:center;gap:14px}
  .logo-mark{width:26px;height:26px;background:var(--brand)}
  .logo-name{font-family:"Montserrat",Arial,sans-serif;font-weight:800;font-size:30px;color:var(--brand)}
  .body-panel{position:absolute;left:0;top:460px;width:880px;height:540px;background:var(--sky)}
  .fee-band{position:absolute;left:380px;top:400px;width:500px;height:60px;background:var(--navy);color:var(--white);font-family:"Montserrat",Arial,sans-serif;font-weight:700;font-size:26px;display:flex;align-items:center;justify-content:center;padding-left:40px}
  .headline{position:absolute;left:0;top:400px;width:440px;height:120px;background:var(--yellow);clip-path:polygon(0 0,88% 0,100% 50%,88% 100%,0 100%);padding:18px 0 0 40px;font-family:"Montserrat",Arial,sans-serif;font-weight:900;font-size:34px;line-height:1.12;color:var(--navy);text-transform:uppercase}
  .intro{position:absolute;left:40px;top:540px;width:800px;font-size:16px;line-height:1.45;color:var(--ink)}
  .offer-list{position:absolute;left:40px;top:610px;width:460px}
  .offer-title{font-family:"Montserrat",Arial,sans-serif;font-weight:800;font-size:20px;color:var(--navy);margin-bottom:8px}
  .offer-list ul{list-style:none}
  .offer-list li{font-size:15.5px;font-weight:600;line-height:1.78;display:flex;align-items:center;gap:10px}
  .offer-list li svg{flex:none}
  .perks{position:absolute;left:520px;top:605px;width:330px;display:flex;flex-direction:column;gap:18px}
  .perk{height:96px;background:var(--navy);color:var(--white);font-family:"Montserrat",Arial,sans-serif;font-weight:800;font-size:18px;line-height:1.3;text-transform:uppercase;display:flex;align-items:center;justify-content:center;text-align:center;padding:0 30px;clip-path:polygon(0 0,100% 0,94% 50%,100% 100%,0 100%,6% 50%)}
  .restrictions{position:absolute;left:640px;top:958px;width:240px;height:42px;background:var(--yellow);clip-path:polygon(8% 0,100% 0,100% 100%,0 100%);font-size:13px;color:var(--navy);display:flex;align-items:center;justify-content:center;padding-left:14px}
  .license-band{position:absolute;left:0;top:1000px;width:460px;height:44px;background:var(--navy);color:var(--white);font-family:"Montserrat",Arial,sans-serif;font-weight:600;font-size:16px;display:flex;align-items:center;padding-left:40px}
  .contact{position:absolute;top:1070px;display:flex;align-items:center;gap:12px;font-size:15px;line-height:1.35;color:var(--ink)}
  .contact-address{left:40px}
  .contact-phone{left:360px;font-family:"Montserrat",Arial,sans-serif;font-weight:800;font-size:22px;color:var(--navy)}
  .contact-web{left:590px;font-size:14px}
  .icon-dot{width:34px;height:34px;border-radius:50%;background:var(--navy);display:flex;align-items:center;justify-content:center;flex:none}
</style>
</head>
<body>
<main class="flyer">
  <div class="photo-team" role="img" aria-label="Photo of four smiling real estate agents in business attire with arms crossed"></div>
  <div class="photo-house" role="img" aria-label="Photo of a two-storey suburban house with trees"></div>

  <div class="logo">
    <span class="logo-mark"></span>
    <span class="logo-name">Veltra Homes</span>
  </div>

  <div class="body-panel"></div>
  <div class="fee-band">$450 Flat Transaction FEE</div>
  <h1 class="headline">100% Commission<br>No Monthly Fee</h1>

  <p class="intro">We are a real estate brokerage looking to hire more real estate agents. We need to list everything we have to offer as a company so real estate agents will join our company.</p>

  <section class="offer-list">
    <h2 class="offer-title">What We Offer:</h2>
    <ul>
      <li><svg width="8" height="12" viewBox="0 0 8 12"><path d="M1 1l5 5-5 5" fill="none" stroke="#2a3a7e" stroke-width="2.4"/></svg>24/7 Office Access</li>
      <li><svg width="8" height="12" viewBox="0 0 8 12"><path d="M1 1l5 5-5 5" fill="none" stroke="#2a3a7e" stroke-width="2.4"/></svg>Free E &amp; O Insurance for 1st Year</li>
      <li><svg width="8" height="12" viewBox="0 0 8 12"><path d="M1 1l5 5-5 5" fill="none" stroke="#2a3a7e" stroke-width="2.4"/></svg>Free Online CE and PLE</li>
      <li><svg width="8" height="12" viewBox="0 0 8 12"><path d="M1 1l5 5-5 5" fill="none" stroke="#2a3a7e" stroke-width="2.4"/></svg>Free 1,000 Business Cards</li>
      <li><svg width="8" height="12" viewBox="0 0 8 12"><path d="M1 1l5 5-5 5" fill="none" stroke="#2a3a7e" stroke-width="2.4"/></svg>Free Professional Social Media Marketing</li>
      <li><svg width="8" height="12" viewBox="0 0 8 12"><path d="M1 1l5 5-5 5" fill="none" stroke="#2a3a7e" stroke-width="2.4"/></svg>Free Printing, Scanning, and Copies</li>
      <li><svg width="8" height="12" viewBox="0 0 8 12"><path d="M1 1l5 5-5 5" fill="none" stroke="#2a3a7e" stroke-width="2.4"/></svg>Free Buyer and Seller Presentation Packages</li>
      <li><svg width="8" height="12" viewBox="0 0 8 12"><path d="M1 1l5 5-5 5" fill="none" stroke="#2a3a7e" stroke-width="2.4"/></svg>Free Papervane Cloud Based Document</li>
      <li style="padding-left:18px">Management Access</li>
      <li><svg width="8" height="12" viewBox="0 0 8 12"><path d="M1 1l5 5-5 5" fill="none" stroke="#2a3a7e" stroke-width="2.4"/></svg>Access to our Internal Brokerage Forum</li>
      <li><svg width="8" height="12" viewBox="0 0 8 12"><path d="M1 1l5 5-5 5" fill="none" stroke="#2a3a7e" stroke-width="2.4"/></svg>Company Profit Sharing!</li>
      <li><svg width="8" height="12" viewBox="0 0 8 12"><path d="M1 1l5 5-5 5" fill="none" stroke="#2a3a7e" stroke-width="2.4"/></svg>Private Offices Available to Rent</li>
    </ul>
  </section>

  <section class="perks">
    <div class="perk">Lead Generation Software with over 3,000 Leads*</div>
    <div class="perk">10 Leads to Start*</div>
    <div class="perk">Free Personal CRM and Website*</div>
  </section>

  <div class="restrictions">*Restrictions and Rules apply</div>

  <div class="license-band">Licensed in: D.C., Maryland &amp; Virginia</div>

  <div class="contact contact-address">
    <span class="icon-dot"><svg width="14" height="18" viewBox="0 0 14 18"><path d="M7 1a6 6 0 0 0-6 6c0 4.5 6 10 6 10s6-5.5 6-10a6 6 0 0 0-6-6z" fill="#fff"/><circle cx="7" cy="7" r="2.3" fill="#2a3a7e"/></svg></span>
    <span>4817 Marlow Creek Road<br>Suite 412, Fairfax, VA 22147</span>
  </div>
  <div class="contact contact-phone">
    <span class="icon-dot"><svg width="16" height="16" viewBox="0 0 16 16"><path d="M3.5 1.5l2.5 3-1.5 1.8a9 9 0 0 0 5.2 5.2L11.5 10l3 2.5-1.6 2.2C7 14.5 1.5 9 1.3 3.1z" fill="#fff"/></svg></span>
    <span>703-241-7086</span>
  </div>
  <div class="contact contact-web">
    <span class="icon-dot"><svg width="18" height="18" viewBox="0 0 18 18" fill="none" stroke="#fff" stroke-width="1.5"><circle cx="9" cy="9" r="7"/><ellipse cx="9" cy="9" rx="3" ry="7"/><path d="M2 9h14"/></svg></span>
    <span>info@veltrahomes.example<br>www.Veltrahomes.example</span>
  </div>
</main>
</body>
</html>
```